Baseline Court Partners needs a business card

I need a business card design for a new company
For the last 10 years I have ran a tennis management company called Silver Ridge Racquet (www.silverridgeracquet.example)
The new company - Baseline Court Partners (BCP) will replace SRRA starting this winter
The goal of BCP will be to expand our operations into new clubs as well and a revenue stream from existing clubs with courtdeskhub.example
We plan to go regional in 2014 and then look outward from there

Target Market(s)

small to medium sized tennis facilities both public and private
Our market are the clubs - not the players
This includes private clubs, municipalities, recreation assc, etc

Industry/Entity Type

Business

Requirements
Must have
• Glen Harwick
• President
• 555-204-1839 Office
• 555-317-9052 Cell
• gharwick@baselinecourtpartners.example
• www.baselinecourtpartnres.example
Nice to have
• One of the unique benefits to a company joining BCP will be integration into our web based club software service - Courtdeskhub.example
• We have developed this turnkey service for small to medium sized clubs and re the exclusive providers of it
Should not have
• address or state

```html
<!DOCTYPE html>
<html lang="en">
<head>
<meta charset="utf-8">
<title>Baseline Court Partners – Business Card</title>
<link rel="stylesheet" href="https://fonts.googleapis.com/css2?family=Open+Sans:wght@400;600;700&display=swap">
<style>
  :root {
    --canvas: #ffffff;
    --slate: #3a3d45;
    --slate-line: rgba(255,255,255,0.035);
    --paper: #d9dadb;
    --paper-line: rgba(255,255,255,0.45);
    --ink: #3a3d45;
    --white: #ffffff;
    --gold: #f2c511;
  }
  * { box-sizing: border-box; margin: 0; padding: 0; }
  html, body { width: 1200px; height: 1000px; overflow: hidden; }
  body {
    background: var(--canvas);
    font-family: "Open Sans", Arial, sans-serif;
    position: relative;
  }
  .card {
    position: absolute;
    left: 250px;
    width: 700px;
    height: 420px;
    overflow: hidden;
    box-shadow: 0 6px 18px rgba(0,0,0,0.18);
  }
  .card--front {
    top: 50px;
    background:
      repeating-linear-gradient(180deg, transparent 0 34px, var(--slate-line) 34px 36px),
      var(--slate);
  }
  .card--back {
    top: 530px;
    background:
      repeating-linear-gradient(180deg, transparent 0 34px, var(--paper-line) 34px 36px),
      var(--paper);
  }

  /* Front */
  .brand-lockup {
    position: absolute;
    left: 150px;
    top: 170px;
    display: flex;
    align-items: center;
    gap: 18px;
  }
  .brand-lockup__dot {
    width: 34px; height: 34px; border-radius: 50%;
    background: var(--gold);
  }
  .brand-lockup__name {
    font-size: 52px;
    font-weight: 700;
    color: var(--white);
    letter-spacing: -0.5px;
  }
  .card__url {
    position: absolute;
    bottom: 22px;
    font-size: 17px;
    font-weight: 700;
  }
  .card--front .card__url { color: var(--white); left: 40px; }
  .card--back .card__url { color: var(--ink); right: 22px; }

  .mini-brand {
    position: absolute;
    right: 24px;
    bottom: 58px;
    display: flex;
    align-items: center;
    gap: 5px;
    font-size: 12px;
    font-weight: 700;
  }
  .mini-brand__dot { width: 8px; height: 8px; border-radius: 50%; }
  .card--front .mini-brand { color: var(--white); }
  .card--front .mini-brand__dot { background: var(--white); }
  .card--back .mini-brand { color: var(--ink); }
  .card--back .mini-brand__dot { background: var(--ink); }

  /* Back */
  .side-band {
    position: absolute;
    left: 0; top: 0;
    width: 126px; height: 100%;
  }
  .company-name {
    position: absolute;
    left: 166px;
    top: 34px;
    font-size: 40px;
    font-weight: 700;
    line-height: 1.12;
    color: var(--ink);
  }
  .person {
    position: absolute;
    left: 166px;
    top: 104px;
    color: var(--ink);
  }
  .person__name { font-size: 24px; font-weight: 700; line-height: 1.2; }
  .person__title { font-size: 17px; font-weight: 600; line-height: 1.3; }
  .contact-list {
    position: absolute;
    left: 166px;
    top: 196px;
    list-style: none;
    color: var(--ink);
    font-size: 18px;
    font-weight: 700;
  }
  .contact-list li { display: flex; margin-bottom: 10px; line-height: 1.4; }
  .contact-list .label { width: 96px; }
  .contact-list .value { font-weight: 600; }
</style>
</head>
<body>

  <section class="card card--front" aria-label="Card front">
    <div class="brand-lockup">
      <span class="brand-lockup__dot"></span>
      <span class="brand-lockup__name">courtdeskhub</span>
    </div>
    <div class="mini-brand"><span class="mini-brand__dot"></span>courtdeskhub</div>
    <p class="card__url">www.baselinecourtpartnres.example</p>
  </section>

  <section class="card card--back" aria-label="Card back">
    <svg class="side-band" viewBox="0 0 126 420" aria-hidden="true">
      <path d="M0 0 H88 V140 A70 70 0 0 1 88 280 V420 H0 Z" fill="var(--slate)"/>
    </svg>
    <h1 class="company-name">Baseline Court Partners</h1>
    <div class="person">
      <p class="person__name">Glen Harwick</p>
      <p class="person__title">President</p>
    </div>
    <ul class="contact-list">
      <li><span class="label">OFFICE :</span><span class="value">555-204-1839</span></li>
      <li><span class="label">CELL :</span><span class="value">555-317-9052</span></li>
      <li><span class="label">EMAIL :</span><span class="value">gharwick@baselinecourtpartners.example</span></li>
    </ul>
    <div class="mini-brand"><span class="mini-brand__dot"></span>courtdeskhub</div>
    <p class="card__url">www.baselinecourtpartnres.example</p>
  </section>

</body>
</html>
```